B2B telecom company need web design

We need a web design for our corporate web site. The company exists since almost 10 years.
This is a DESIGN contest, you're expected to provide design only, NOT the whole website. The winner will have to provide the HTML template (with Lorem Ipsum content) and the CSS files of his design.
Our initial product is SMS peering in P2P (you send a SMS to a friend in a foreign country, great chance that your operator route your SMS to us that we route to the recipient). We're launching a bulk SMS service (marketing and application to SMS).
Target is mostly corporate, usually big corporate (operators, contents providers...) where use of SMS is part of the main business.
The web site is composed of 1 landing page and 7 content pages (plan is given for your information, all content page are using the same template and the same design, you do NOT need to make one design per page) :
* About US
Company Profile
They trust us
The Volnor Team
Partners
Contact us
* Solution
P2P SMS
A2P SMS
You only need to submit the landing page and a template page for the content (with h1, h2, h3 and h4).
Design must be based on our new logo (see attached file).
Our current web site http://www.volnor-example.com
The winner of the contest will have to provide state of the art HTML template and CSS files of his design. Photo used shall be downloaded from Pixelbrook (provide the ID of the picture that we purchase file).
Target Market(s)
Telecom operator. SMS Peering hubs. Bulk SMS.
Industry/Entity Type
It Company
Number of Pages Required
2 page

```html
<!DOCTYPE html>
<html lang="en">
<head>
<meta charset="utf-8">
<title>Volnor mobile — We connect you creatively</title>
<link rel="stylesheet" href="https://fonts.googleapis.com/css2?family=Open+Sans:wght@300;400;700;800&display=swap">
<style>
  :root {
    --ink-white: #ffffff;
    --hero-warm: #d9d2cb;
    --hero-grey: #b9b6b3;
    --hero-sweater: #9c968e;
    --hero-blue: #6f8fb8;
    --hero-red: #e9a49b;
    --hero-light: #f2eeea;
    --ring: rgba(255, 255, 255, 0.22);
    --shade: rgba(0, 0, 0, 0.18);
  }
  * { margin: 0; padding: 0; box-sizing: border-box; }
  html, body { width: 1200px; height: 800px; overflow: hidden; }
  body { font-family: "Open Sans", Arial, sans-serif; color: var(--ink-white); background: var(--hero-light); }

  .landing { position: relative; width: 1200px; height: 800px; overflow: hidden; }

  .hero-photo {
    position: absolute; inset: 0;
    background:
      radial-gradient(ellipse 380px 300px at 30% 35%, var(--hero-warm), transparent 70%),
      radial-gradient(ellipse 320px 260px at 20% 75%, var(--hero-sweater), transparent 70%),
      radial-gradient(ellipse 260px 220px at 50% 30%, var(--hero-blue), transparent 70%),
      radial-gradient(ellipse 300px 260px at 82% 70%, var(--hero-red), transparent 70%),
      linear-gradient(100deg, var(--hero-grey) 0%, var(--hero-warm) 45%, var(--hero-light) 100%);
  }
  .hero-shade { position: absolute; inset: 0; background: var(--shade); }

  .hero-rings { position: absolute; left: 0; top: 0; width: 1200px; height: 800px; }

  .site-header {
    position: absolute; top: 40px; left: 60px; right: 60px;
    display: flex; justify-content: space-between; align-items: flex-start;
  }
  .brand { font-size: 26px; font-weight: 300; letter-spacing: 1px; }
  .main-nav { display: flex; gap: 30px; margin-top: 48px; }
  .main-nav a { color: var(--ink-white); text-decoration: none; font-size: 16px; font-weight: 400; }

  .hero-copy {
    position: absolute; left: 0; right: 0; top: 330px;
    text-align: center; padding-left: 120px;
  }
  .hero-title { font-size: 52px; font-weight: 800; letter-spacing: -0.5px; text-transform: uppercase; }
  .hero-tagline { margin-top: 10px; font-size: 18px; font-weight: 400; letter-spacing: 1px; text-transform: uppercase; }

  .scroll-cue { position: absolute; left: 50%; bottom: 28px; transform: translateX(-50%); }
</style>
</head>
<body>
  <main class="landing">
    <div class="hero-photo" role="img" aria-label="Photo of a smiling father and young son looking at a mobile phone together on a bus"></div>
    <div class="hero-shade"></div>

    <svg class="hero-rings" viewBox="0 0 1200 800" aria-hidden="true">
      <circle cx="600" cy="330" r="110" fill="none" stroke="var(--ring)" stroke-width="22"/>
      <circle cx="600" cy="330" r="170" fill="none" stroke="var(--ring)" stroke-width="14" opacity="0.6"/>
    </svg>

    <header class="site-header">
      <div class="brand">VOLNOR mobile</div>
      <nav class="main-nav">
        <a href="#">About</a>
        <a href="#">Services</a>
        <a href="#">Why us</a>
        <a href="#">News</a>
        <a href="#">Contact</a>
      </nav>
    </header>

    <section class="hero-copy">
      <h1 class="hero-title">We connect you creatively</h1>
      <p class="hero-tagline">Marketers . Innovaters . Consultants</p>
    </section>

    <svg class="scroll-cue" width="28" height="28" viewBox="0 0 28 28" aria-hidden="true">
      <circle cx="14" cy="14" r="12" fill="none" stroke="var(--ink-white)" stroke-width="2" opacity="0.8"/>
      <path d="M9 12 L14 17 L19 12" fill="none" stroke="var(--ink-white)" stroke-width="2" opacity="0.8"/>
    </svg>
  </main>
</body>
</html>
```